Ductless Mini Split Business Website

Amber Kite Services is looking to design an eye catching educational website about installing Ductless mini splits.

Similar to this company.
https://www.cedarcoolair.com/

```html
<!DOCTYPE html>
<html lang="en">
<head>
<meta charset="utf-8">
<title>Contact – Amber Kite Services</title>
<link href="https://fonts.googleapis.com/css2?family=Rubik:wght@300;400;500&display=swap" rel="stylesheet">
<style>
:root{
  --ink:#222222;
  --text:#444444;
  --muted:#888888;
  --accent:#f9c416;
  --cream:#fffac8;
  --line:#d8d8d8;
  --footer-rule:#f6eecf;
  --social-blue:#3b5998;
  --social-red:#d32323;
  --social-gold:#f5c518;
  --social-crimson:#e62117;
  --map-fill:#e6ebe2;
}
*{margin:0;padding:0;box-sizing:border-box}
html,body{width:828px;height:1200px;overflow:hidden;background:#fff}
body{position:relative;font-family:"Rubik",sans-serif;color:var(--text)}
.abs{position:absolute}
.hero-shape{position:absolute;left:0;top:0}
.brand{left:26px;top:20px;display:flex;align-items:center;gap:7px}
.brand-dot{width:16px;height:16px;border-radius:50%;background:var(--accent)}
.brand-name{font-size:12px;font-weight:500;color:var(--ink);line-height:1.15;width:80px}
.nav{top:24px;left:252px;font-size:10.5px;color:var(--ink);font-weight:300}
.nav a{position:absolute;white-space:nowrap;color:var(--ink);text-decoration:none}
.nav .caret{font-size:7px;margin-left:3px}
.nav .current{border-bottom:1.5px solid var(--accent);padding-bottom:4px}
.page-title{left:74px;top:112px;font-size:37px;font-weight:400;color:var(--ink)}
.crumbs{left:74px;top:162px;font-size:10.5px;color:var(--ink);font-weight:300}
.crumbs span.now{color:var(--muted)}
.intro{left:74px;top:252px;font-size:15px;line-height:20px;color:var(--ink);font-weight:300}
.field{position:absolute;border:1px solid var(--line);border-radius:16px;height:31px;width:215px;padding:10px 12px;font-size:8.5px;color:#555;font-weight:300}
.field.msg{height:67px;width:448px;border-radius:18px;padding-top:14px}
.submit{left:74px;top:519px;width:98px;height:31px;border-radius:16px;background:#fff;box-shadow:0 6px 18px rgba(120,150,200,.18);color:var(--accent);font-size:10px;display:flex;align-items:center;justify-content:center}
.side-head{left:599px;top:279px;font-size:15px;color:var(--ink)}
.side-addr{left:599px;top:308px;font-size:9.5px;line-height:15px;font-weight:300}
.side-phone{left:599px;top:365px;font-size:17px;color:var(--accent);font-weight:300}
.map{left:74px;top:604px;width:681px;height:307px;background:var(--map-fill)}
.footer-rule{left:0;top:971px;width:828px;height:1px;background:var(--footer-rule)}
.f-head{top:1018px;font-size:13.5px;color:var(--ink);white-space:nowrap}
.f-text{font-size:8.5px;line-height:17.5px;font-weight:300}
.f-links a{display:block;font-size:8.5px;line-height:21px;color:var(--text);text-decoration:none;font-weight:300}
.f-phone{left:108px;top:1105px;font-size:16px;color:var(--accent);font-weight:300}
.social{left:527px;top:1105px;display:flex;gap:5px}
.social span{width:22px;height:22px;border-radius:50%}
.to-top{left:756px;top:1144px;width:28px;height:28px;border-radius:50%;background:var(--accent);display:flex;align-items:center;justify-content:center}
.copy{left:99px;top:1172px;font-size:8px;color:var(--ink);font-weight:300}
</style>
</head>
<body>
<svg class="hero-shape" width="828" height="170" viewBox="0 0 828 170" aria-hidden="true">
  <path d="M166,0 L828,0 L828,66 L400,156 Q372,163 346,150 L186,56 Q164,40 166,0 Z" fill="var(--cream)"/>
</svg>

<header>
  <div class="abs brand"><span class="brand-dot"></span><span class="brand-name">Amber Kite Services</span></div>
  <nav class="abs nav">
    <a style="left:0">Home</a>
    <a style="left:46px">About<span class="caret">&#9662;</span></a>
    <a style="left:104px">Ductless Heat Pumps<span class="caret">&#9662;</span></a>
    <a style="left:236px">Ductless Heat Pumps FAQ</a>
    <a style="left:381px">Financing</a>
    <a style="left:447px">Reviews</a>
    <a style="left:505px" class="current">Contact</a>
  </nav>
</header>

<h1 class="abs page-title">Contact</h1>
<div class="abs crumbs">
  <svg width="9" height="8" viewBox="0 0 10 9" style="vertical-align:-1px"><path d="M5 0 L10 4.5 H8.5 V9 H6 V6 H4 V9 H1.5 V4.5 H0 Z" fill="var(--ink)"/></svg>
  Home &nbsp;&rsaquo;&nbsp; <span class="now">Contact</span>
</div>

<main>
  <p class="abs intro">Thank you for your interest.<br>Please fill out the form below to inquire.</p>
  <div class="field" style="left:74px;top:323px">Name</div>
  <div class="field" style="left:307px;top:323px">Email</div>
  <div class="field" style="left:74px;top:372px">Phone</div>
  <div class="field" style="left:307px;top:372px">Organization</div>
  <div class="field msg" style="left:74px;top:424px">Message</div>
  <div class="abs submit">Contact Us</div>

  <h2 class="abs side-head" style="font-weight:400">Location</h2>
  <p class="abs side-addr">2870 SE Harbor Loop,<br>Suite B214<br>Clackamas, OR 97015</p>
  <p class="abs side-phone">(503) 555-0184</p>

  <div class="abs map" role="img" aria-label="Street map showing the office location"></div>
</main>

<footer>
  <div class="abs footer-rule"></div>
  <h3 class="abs f-head" style="left:108px;font-weight:400">Location</h3>
  <p class="abs f-text" style="left:108px;top:1046px">2870 SE Harbor Loop,<br>Suite B214<br>Clackamas, OR 97015</p>
  <p class="abs f-phone">(503) 555-0184</p>

  <h3 class="abs f-head" style="left:265px;font-weight:400">Amber Kite Services</h3>
  <div class="abs f-links" style="left:265px;top:1042px">
    <a>Home</a><a>About</a><a>Ductless Heat Pumps</a><a>Ductless Heat Pumps FAQ</a>
  </div>

  <h3 class="abs f-head" style="left:422px;font-weight:400">Quick Link</h3>
  <div class="abs f-links" style="left:422px;top:1042px">
    <a>Financing</a><a>Contact Us</a><a>Privacy Policy</a><a>Sitemap</a>
  </div>

  <h3 class="abs f-head" style="left:528px;font-weight:400">About Us</h3>
  <p class="abs f-text" style="left:528px;top:1046px;width:200px">Experience maximum comfort, better indoor air quality, and lower utility bills by installing ductless heat pumps in your home.</p>
  <div class="abs social" aria-label="Social links">
    <span style="background:var(--social-blue)"></span>
    <span style="background:var(--social-red)"></span>
    <span style="background:var(--social-gold)"></span>
    <span style="background:var(--social-crimson)"></span>
  </div>

  <div class="abs to-top"><svg width="10" height="7" viewBox="0 0 10 7"><path d="M1 6 L5 2 L9 6" stroke="#fff" stroke-width="1.6" fill="none"/></svg></div>
  <p class="abs copy">Copyright ©2019 | All rights reserved</p>
</footer>
</body>
</html>
```